farvinta labs cybersecurity website design and development

website design and development for a cybersecurity company. we have a logo and would like site to suit logo colors and look
cybersecurity website should be secure and look professional
main example of site we want to use: https://www.plomvex.example/
site should be usable on tablet and phones

For each design proposal, please could you provide details of what language you'll use to code the website.

Target Market(s)

insurance companies, financial institutions, private SME, Africa and Europe

Coding

Coded - Design and coding required

Number of Pages Required

5+ page

Requirements
Must have
• 9 Pages:
Home
About us
Contacts
Partners
Blog
Services
( consulting, vulnerability assessment, information systems security audit, ISO compliance, Penetration testing, security awareness training, social engineering test, protection against DDoS, procurement )
Resources
Technologies
Careers
Nice to have
• nice to have all services have their own pages.
design based on logo colors and look

please provide what will be use to code the website

```html
<!DOCTYPE html>
<html lang="en">
<head>
<meta charset="utf-8">
<title>Farvinta Labs — Cybersecure Your Business</title>
<link href="https://fonts.googleapis.com/css2?family=Maven+Pro:wght@400;500;600;700&family=Poppins:wght@300;400;500&display=swap" rel="stylesheet">
<style>
:root{
  --navy:#1d3389;
  --blue:#0a90dc;
  --text:#555b66;
  --muted:#7d8590;
  --pale:#e6eef6;
  --footer:#e1eaf3;
  --white:#fff;
  --line:#c9d3dd;
}
*{box-sizing:border-box;margin:0;padding:0}
html,body{width:1200px;height:2542px;overflow:hidden}
body{font-family:"Poppins",sans-serif;color:var(--text);background:var(--white);position:relative}
h1,h2,h3,h4,.brand,.btn{font-family:"Maven Pro",sans-serif}
a{color:inherit;text-decoration:none}

.site-header{height:75px;display:flex;align-items:center;padding:0 60px;justify-content:space-between}
.brand{display:flex;align-items:center;gap:10px;font-size:22px;font-weight:600;color:var(--navy);white-space:nowrap}
.brand-mark{width:38px;height:38px;border-radius:50%;background:var(--navy)}
.main-nav{display:flex;gap:17px;font-size:11.5px;color:#333;margin-left:80px;white-space:nowrap}
.main-nav .active{color:var(--blue);position:relative}
.main-nav .active::after{content:"";position:absolute;left:50%;top:20px;margin-left:-5px;border:5px solid transparent;border-bottom-color:var(--blue)}
.phone-btn{background:var(--blue);color:var(--white);border-radius:8px;padding:9px 12px;font-family:"Maven Pro",sans-serif;font-size:16px;font-weight:600;display:flex;align-items:center;gap:6px;white-space:nowrap}

.hero{height:600px;background:linear-gradient(100deg,#dbe6ee 0%,#c7d7e2 55%,#afc3d0 100%);position:relative}
.hero-copy{position:absolute;left:118px;top:145px}
.hero-kicker{font-size:21px;color:#333;font-weight:400}
.hero-title{font-size:68px;font-weight:700;color:var(--navy);line-height:1.1;margin-top:6px;white-space:nowrap}
.hero-title span{color:var(--blue);font-weight:500}
.hero-sub{font-size:23px;color:#2c3340;margin-top:8px;font-family:"Maven Pro",sans-serif}
.hero-text{font-size:13px;line-height:20px;margin-top:16px;color:#3c4350;width:410px}
.btn{display:inline-block;background:var(--blue);color:var(--white);font-weight:600;border-radius:8px;font-size:16px;padding:11px 21px}
.hero .btn{margin-top:18px}
.hero-art{position:absolute;left:630px;top:100px;width:460px;height:400px;border-radius:50%;background:radial-gradient(circle,#ffffff 0 22%,#7fb3da 23% 30%,rgba(40,120,200,.25) 31% 60%,rgba(255,255,255,0) 61%)}
.dots{position:absolute;left:118px;top:555px;display:flex;gap:9px}
.dots i{width:13px;height:13px;border-radius:50%;background:var(--white)}
.dots i.on{background:transparent;border:2px solid var(--blue)}

.partners{height:115px;display:flex;align-items:center;justify-content:center;gap:40px;position:relative}
.partner{height:38px;border-radius:6px;background:#c8ced6}
.chev{position:absolute;top:46px}

.welcome{height:420px;position:relative}
.welcome-copy{position:absolute;left:170px;top:75px;width:380px}
.eyebrow{font-family:"Maven Pro",sans-serif;font-size:16px;color:var(--muted)}
.welcome h2{font-size:33px;color:var(--navy);font-weight:600;margin:8px 0 18px}
.welcome p{font-size:12px;line-height:20.5px;margin-bottom:11px}
.welcome .btn{margin-top:7px;padding:11px 19px}
.welcome-media{position:absolute;left:665px;top:100px;width:375px;height:206px;background:radial-gradient(circle at 55% 50%,#4a9fe0 0%,#154a8a 35%,#071a38 80%)}

.services{height:525px;background:var(--pale);text-align:center;padding-top:70px;position:relative}
.services h2,.contact h2{font-size:32px;color:var(--navy);font-weight:600;margin-top:6px}
.cards{display:flex;gap:15px;justify-content:center;margin-top:40px}
.card{width:219px;height:270px;background:var(--white);border-radius:6px;padding:22px 16px}
.card svg.icon{width:60px;height:60px}
.card h3{font-size:16px;color:var(--navy);font-weight:600;margin-top:18px;height:44px;line-height:20px}
.card p{font-size:11.5px;line-height:19px;margin-top:12px}
.card a{display:inline-block;margin-top:13px;font-family:"Maven Pro",sans-serif;font-size:12px;color:var(--blue);text-decoration:underline;font-weight:600}
.services .chev{top:300px}

.contact{height:440px;text-align:center;padding-top:65px}
.contact .lead{font-size:14px;margin-top:10px}
.form{position:relative;width:650px;height:150px;margin:30px auto 0;text-align:left}
.field{position:absolute;border:1px solid var(--line);border-radius:6px;font-size:11.5px;color:#666;padding:0 13px;display:flex;align-items:center;background:var(--white)}
.field.focus{border-color:var(--blue);color:var(--blue)}
.contact .btn{margin-top:16px;padding:11px 22px}

.site-footer{position:absolute;left:0;top:2175px;width:1200px;height:367px;background:var(--footer);padding:40px 61px 0}
.cols{display:flex}
.col{width:275px}
.col h4{font-size:17px;color:var(--navy);font-weight:600;margin-bottom:14px}
.col li{list-style:none;font-size:12px;line-height:22.6px;color:#4a5260}
.touch{display:flex;align-items:center;gap:10px;margin-bottom:10px;font-size:12px;color:#333}
.touch .ico{width:34px;height:34px;border-radius:50%;background:var(--navy);display:flex;align-items:center;justify-content:center;flex:none}
.touch.big{font-size:16px;font-weight:500}
.social{display:flex;gap:14px;margin-top:14px}
.social i{width:16px;height:16px;border-radius:50%;background:var(--blue)}
.copyright{position:absolute;left:61px;right:61px;top:330px;border-top:1px solid #d0dae4;padding-top:14px;text-align:center;font-size:12px;color:#333}
.copyright span{color:var(--blue)}
</style>
</head>
<body>
<header class="site-header">
  <a class="brand"><span class="brand-mark"></span>Farvinta Labs</a>
  <nav class="main-nav">
    <a class="active">HOME</a><a>ABOUT US</a><a>SERVICES</a><a>PARTNERS</a><a>BlOG</a><a>RESOURCES</a><a>TECHNOLOGIES</a><a>CAREERS</a><a>CONTACT US</a>
  </nav>
  <a class="phone-btn"><svg width="18" height="18" viewBox="0 0 24 24"><path fill="#fff" d="M6.6 10.8a15 15 0 0 0 6.6 6.6l2.2-2.2a1 1 0 0 1 1-.25 11.4 11.4 0 0 0 3.6.57 1 1 0 0 1 1 1V20a1 1 0 0 1-1 1A17 17 0 0 1 3 4a1 1 0 0 1 1-1h3.5a1 1 0 0 1 1 1c0 1.25.2 2.45.57 3.57a1 1 0 0 1-.25 1z"/></svg>555 014 2290</a>
</header>

<section class="hero">
  <div class="hero-copy">
    <p class="hero-kicker">GET HIGH QUALITY</p>
    <h1 class="hero-title">Farvinta <span>Labs</span></h1>
    <p class="hero-sub">Cybersecure Your Business</p>
    <p class="hero-text">Lorem Ipsum has been the industry's standard dummy text ever since the 1500s, when an unknown printer.</p>
    <a class="btn">CONTACT US</a>
  </div>
  <div class="hero-art" role="img" aria-label="Circuit board lines radiating from a secure padlock shield emblem"></div>
  <div class="dots"><i></i><i></i><i></i><i class="on"></i><i></i></div>
</section>

<section class="partners">
  <svg class="chev" style="left:100px" width="14" height="26" viewBox="0 0 14 26"><path d="M12 1 2 13l10 12" fill="none" stroke="#999" stroke-width="1.5"/></svg>
  <div class="partner" style="width:120px"></div>
  <div class="partner" style="width:58px;border-radius:50%;height:46px"></div>
  <div class="partner" style="width:125px"></div>
  <div class="partner" style="width:64px"></div>
  <div class="partner" style="width:112px"></div>
  <div class="partner" style="width:72px"></div>
  <div class="partner" style="width:90px"></div>
  <svg class="chev" style="left:1097px" width="14" height="26" viewBox="0 0 14 26"><path d="m2 1 10 12L2 25" fill="none" stroke="#999" stroke-width="1.5"/></svg>
</section>

<section class="welcome">
  <div class="welcome-copy">
    <p class="eyebrow">Welcome To</p>
    <h2>Farvinta Labs</h2>
    <p>Lorem Ipsum has been the industry's standard dummy text ever since the 1500s, when an unknown printer took a galley of type and scrambled it to make a type specimen book.</p>
    <p>Lorem Ipsum has been the industry's standard dummy text ever since the 1500s, when an unknown printer took a galley of type and scrambled it to make a type specimen book. It has survived not only five centuries, but also the leap into electronic</p>
    <a class="btn">LEARN MORE</a>
  </div>
  <div class="welcome-media" role="img" aria-label="Hand holding a glowing digital padlock surrounded by network icons"></div>
</section>

<section class="services">
  <p class="eyebrow">What We Offers</p>
  <h2>Our Services</h2>
  <svg class="chev" style="left:95px" width="16" height="38" viewBox="0 0 16 38"><path d="M14 1 2 19l12 18" fill="none" stroke="#777" stroke-width="1.5"/></svg>
  <div class="cards">
    <article class="card">
      <svg class="icon" viewBox="0 0 60 60" fill="none" stroke="var(--navy)" stroke-width="2"><circle cx="14" cy="14" r="5"/><circle cx="30" cy="12" r="5"/><circle cx="46" cy="14" r="5"/><path d="M6 36V26a6 6 0 0 1 6-6h4M54 36V26a6 6 0 0 0-6-6h-4M22 24h16v10H22zM26 34v16M34 34v16"/></svg>
      <h3>Consulting</h3>
      <p>Lorem Ipsum has been the industry's standard dummy text ever since the when</p>
      <a>Read More ▸</a>
    </article>
    <article class="card">
      <svg class="icon" viewBox="0 0 60 60" fill="none" stroke="var(--navy)" stroke-width="2"><rect x="10" y="8" width="32" height="44" rx="2"/><path d="M18 20h18M18 28h18M18 36h12M18 44h10"/><circle cx="44" cy="40" r="8" stroke="var(--blue)"/></svg>
      <h3>Vulnerability<br>Assessment</h3>
      <p>Lorem Ipsum has been the industry's standard dummy text ever since the when</p>
      <a>Read More ▸</a>
    </article>
    <article class="card">
      <svg class="icon" viewBox="0 0 60 60" fill="none" stroke="var(--navy)" stroke-width="2"><path d="M14 6h26v48H14z"/><path d="M20 18h14M20 26h14M20 34h8"/><path d="m30 44 18-20 4 4-18 20-6 2z" stroke="var(--blue)"/></svg>
      <h3>Information Systems<br>Security Audit</h3>
      <p>Lorem Ipsum has been the industry's standard dummy text ever since the when</p>
      <a>Read More ▸</a>
    </article>
    <article class="card">
      <svg class="icon" viewBox="0 0 60 60" fill="none" stroke="var(--navy)" stroke-width="2"><rect x="14" y="6" width="30" height="46" rx="2"/><circle cx="29" cy="22" r="5"/><path d="M21 36h16M21 42h10"/><circle cx="42" cy="44" r="7" stroke="var(--blue)"/><path d="m39 44 2 2 4-4" stroke="var(--blue)"/></svg>
      <h3>ISO<br>Compliance</h3>
      <p>Lorem Ipsum has been the industry's standard dummy text ever since the when</p>
      <a>Read More ▸</a>
    </article>
  </div>
  <svg class="chev" style="left:1094px" width="16" height="38" viewBox="0 0 16 38"><path d="m2 1 12 18L2 37" fill="none" stroke="#777" stroke-width="1.5"/></svg>
</section>

<section class="contact">
  <h2>Contact Us</h2>
  <p class="lead">Ready to see how Cyber Security Services can help?</p>
  <div class="form">
    <div class="field focus" style="left:0;top:0;width:293px;height:42px">Name *</div>
    <div class="field" style="left:0;top:53px;width:293px;height:42px">Email *</div>
    <div class="field" style="left:0;top:105px;width:293px;height:42px">Phone *</div>
    <div class="field" style="left:304px;top:0;width:346px;height:147px;align-items:flex-start;padding-top:12px">Message *</div>
  </div>
  <a class="btn">SUBMIT</a>
</section>

<footer class="site-footer">
  <div class="cols">
    <div class="col"><h4>Services</h4><ul>
      <li>Consulting</li><li>Vulnerability Assessment</li><li>Information Systems Security Audit</li><li>ISO Compliance</li><li>Penetration Testing</li><li>Security Awareness Training</li><li>Social Engineering Test</li><li>Protection Against Ddos</li><li>Procurement</li></ul></div>
    <div class="col"><h4>Resources</h4><ul>
      <li>Blog</li><li>Case Studies</li><li>Wiki</li><li>Specifications</li><li>Practices</li><li>Privacy policy</li><li>Cookies</li></ul></div>
    <div class="col"><h4>Sitemap</h4><ul>
      <li>Home</li><li>About us</li><li>Services</li><li>Partners</li><li>Blog</li><li>Resources</li><li>Technologies</li><li>Career</li><li>Contacts</li></ul></div>
    <div class="col"><h4>Get In Touch</h4>
      <div class="touch"><span class="ico"><svg width="16" height="16" viewBox="0 0 24 24" fill="none" stroke="#fff" stroke-width="2"><path d="M12 22s7-7 7-12a7 7 0 0 0-14 0c0 5 7 12 7 12z"/><circle cx="12" cy="10" r="2.5"/></svg></span>101 - Lorem ipsum simple txet<br>print type industry</div>
      <div class="touch big"><span class="ico"><svg width="16" height="16" viewBox="0 0 24 24"><path fill="#fff" d="M6.6 10.8a15 15 0 0 0 6.6 6.6l2.2-2.2a1 1 0 0 1 1-.25 11.4 11.4 0 0 0 3.6.57 1 1 0 0 1 1 1V20a1 1 0 0 1-1 1A17 17 0 0 1 3 4a1 1 0 0 1 1-1h3.5a1 1 0 0 1 1 1c0 1.25.2 2.45.57 3.57a1 1 0 0 1-.25 1z"/></svg></span>555 014 2290</div>
      <div class="touch"><span class="ico"><svg width="16" height="16" viewBox="0 0 24 24" fill="none" stroke="#fff" stroke-width="2"><rect x="3" y="5" width="18" height="14" rx="2"/><path d="m3 7 9 6 9-6"/></svg></span>info@farvintalabs.com</div>
      <div class="social"><i></i><i></i><i></i></div>
    </div>
  </div>
  <p class="copyright">©<span>Farvinta Labs</span> - 2021 All rights reserved &nbsp;| &nbsp;Privacy Policy &nbsp;| &nbsp;Tearms &amp; Condition</p>
</footer>
</body>
</html>
```